Strength Coach Business Card Design Project

I would like a business card design to complement my new logo. I would like the card to be clean, seek and strong!

Target Market(s)

Mostly adults and junior atheletes who are serious about changing their lives.

Industry/Entity Type

Business

Font styles to use
Serif

Colors

Designer to choose colors to be used in the design.

```html
<!DOCTYPE html>
<html lang="en">
<head>
<meta charset="utf-8">
<title>Ridge Strength and Fitness – Business Card</title>
<link rel="stylesheet" href="https://fonts.googleapis.com/css2?family=Lato:wght@400;900&display=swap">
<style>
  :root {
    --backdrop: #d9d9d9;
    --card-white: #ffffff;
    --charcoal: #333333;
    --brand-red: #e8262a;
    --text-light: #f2f2f2;
  }
  * { margin: 0; padding: 0; box-sizing: border-box; }
  html, body {
    width: 1200px; height: 1000px; overflow: hidden;
    background: var(--backdrop);
    font-family: "Lato", Arial, sans-serif;
  }
  .card {
    position: absolute; left: 100px; top: 215px;
    width: 1000px; height: 571px;
    background: var(--card-white);
    box-shadow: 0 12px 30px rgba(0,0,0,0.25);
    overflow: hidden;
  }
  .card-shapes { position: absolute; inset: 0; }
  .brand {
    position: absolute; left: 60px; top: 130px;
    display: flex; align-items: center; gap: 20px;
  }
  .brand-square {
    width: 56px; height: 56px; background: var(--brand-red);
  }
  .brand-divider {
    width: 3px; height: 140px; background: var(--charcoal);
  }
  .brand-name {
    color: var(--charcoal); font-weight: 900;
    font-size: 34px; line-height: 1.08; text-transform: uppercase;
    letter-spacing: 0.5px; white-space: nowrap;
  }
  .contact {
    position: absolute; right: 40px; top: 238px;
    text-align: right; color: var(--text-light);
  }
  .contact-name {
    color: var(--brand-red); font-size: 30px; font-weight: 400;
    margin-right: 48px;
  }
  .contact-role {
    font-size: 25px; margin-top: 2px; margin-right: 48px;
  }
  .contact-list { list-style: none; margin-top: 26px; }
  .contact-item {
    display: flex; justify-content: flex-end; align-items: center;
    gap: 16px; font-size: 25px; line-height: 44px;
  }
  .contact-item svg { width: 30px; height: 30px; flex: none; }
</style>
</head>
<body>
  <section class="card">
    <svg class="card-shapes" viewBox="0 0 1000 571" preserveAspectRatio="none" aria-hidden="true">
      <path fill="var(--charcoal)" d="M0,480 C250,440 390,400 490,260 C590,120 760,75 1000,60 L1000,571 L0,571 Z"/>
      <path fill="var(--brand-red)" d="M0,462 C250,425 370,385 470,235 C570,90 750,35 1000,15 L1000,42 C760,62 595,115 490,250 C390,395 260,440 0,470 Z"/>
    </svg>

    <div class="brand">
      <div class="brand-square"></div>
      <div class="brand-divider"></div>
      <div class="brand-name">Ridge<br>Strength<br>and Fitness</div>
    </div>

    <div class="contact">
      <p class="contact-name">Marcus Reed</p>
      <p class="contact-role">Strength and Fitness Coach</p>
      <ul class="contact-list">
        <li class="contact-item">0400 123 987
          <svg viewBox="0 0 24 24" aria-label="Phone"><rect x="7" y="3" width="10" height="18" rx="2" fill="none" stroke="var(--brand-red)" stroke-width="2"/><rect x="9" y="6" width="6" height="6" fill="var(--brand-red)"/></svg>
        </li>
        <li class="contact-item">contact@marcus-reed.co
          <svg viewBox="0 0 24 24" aria-label="Email"><rect x="2" y="5" width="20" height="14" fill="var(--brand-red)"/><path d="M2,5 L12,13 L22,5" fill="none" stroke="var(--charcoal)" stroke-width="1.6"/></svg>
        </li>
        <li class="contact-item">www.marcus-reed.co
          <svg viewBox="0 0 24 24" aria-label="Website"><circle cx="12" cy="12" r="10" fill="var(--brand-red)"/><path d="M2,12 H22 M12,2 C7,7 7,17 12,22 M12,2 C17,7 17,17 12,22" fill="none" stroke="var(--charcoal)" stroke-width="1.4"/></svg>
        </li>
      </ul>
    </div>
  </section>
</body>
</html>
```